Virtual assistant company needs letterhead and email signature

We need a letterhead and email signature for our virtual assistant company - taskBeaver (small w capital F). Our tag line is plan ahead | taskBeaver

The colours we would like used are;

#81788c
#dddbe1

For reference our business cards have used #81788c background colour and #dddbe1 text

The fonts we would like used are

Lora
Proxima Nova

Please check out our twitter and facebook for style and feel

Twitter: @taskbeaver
www.examplebook.test/taskbeaver

Please also find attached our landing page and business cards for reference

Any questions please let us know

Thanks
E

Reason: We like the opportunity to receive furthur designs

```html
<!DOCTYPE html>
<html lang="en">
<head>
<meta charset="utf-8">
<title>taskBeaver stationery</title>
<link rel="stylesheet" href="https://fonts.googleapis.com/css2?family=Lora&family=Open+Sans:wght@400;700&display=swap">
<style>
  :root {
    --brand: #81788c;
    --brand-light: #dddbe1;
    --on-brand: #f4f3f6;
    --paper: #ffffff;
    --paper-shade: #efefef;
    --rule: #dcdbdf;
    --ink: #3d3d3d;
    --backdrop: #e6e4e8;
  }
  * { margin: 0; padding: 0; box-sizing: border-box; }
  html, body { width: 771px; height: 1200px; overflow: hidden; }
  body {
    position: relative;
    background: var(--backdrop);
    font-family: "Open Sans", sans-serif;
  }

  /* Letterhead */
  .letterhead {
    position: absolute; left: 20px; top: 14px; width: 735px; height: 951px;
    background: linear-gradient(135deg, var(--paper) 30%, var(--paper-shade) 100%);
    box-shadow: 0 1px 3px rgba(0,0,0,.25);
  }
  .letterhead__header {
    position: absolute; left: 0; top: 0; width: 100%; height: 108px;
    background: var(--brand);
  }
  .letterhead__brand {
    position: absolute; left: 35px; top: 22px;
    font-family: "Lora", serif; font-size: 46px; line-height: 1;
    color: var(--on-brand);
  }
  .letterhead__tagline {
    position: absolute; left: 68px; top: 67px;
    font-size: 14px; color: var(--brand-light); letter-spacing: .2px;
  }
  .letterhead__contact {
    position: absolute; left: 580px; top: 22px;
    border-left: 1px solid var(--brand-light);
    padding-left: 12px;
    font-size: 11.5px; line-height: 14px; color: var(--on-brand);
  }
  .letterhead__contact p + p.gap { margin-top: 9px; }
  .icon { display: inline-block; vertical-align: -1px; margin-right: 3px; }
  .letterhead__footer { position: absolute; left: 0; bottom: 0; }
  .footer-url {
    position: absolute; font-size: 13px; letter-spacing: 3px; color: var(--on-brand);
  }
  .letterhead .footer-url { right: 17px; bottom: 5px; }

  /* Business card */
  .card {
    position: absolute; left: 102px; top: 982px; width: 525px; height: 176px;
    background: var(--paper);
    box-shadow: 0 1px 3px rgba(0,0,0,.25);
  }
  .card__header {
    position: absolute; left: 0; top: 0; width: 100%; height: 40px;
    background: var(--brand);
  }
  .card__brand {
    position: absolute; left: 14px; top: 6px;
    font-family: "Lora", serif; font-size: 22px; line-height: 1; color: var(--on-brand);
  }
  .card__tagline {
    position: absolute; left: 30px; top: 28px; font-size: 6.5px; color: var(--brand-light);
  }
  .card__name {
    position: absolute; right: 17px; top: 10px;
    font-weight: 700; font-size: 15px; color: var(--on-brand);
  }
  .card__contact {
    position: absolute; left: 13px; top: 97px;
    font-size: 12.5px; line-height: 21px; color: var(--ink);
  }
  .card__contact .address { margin-top: 3px; }
  .card__footer { position: absolute; left: 0; bottom: 0; }
  .card .footer-url { right: 12px; bottom: 3px; font-size: 12.5px; letter-spacing: 3px; }
</style>
</head>
<body>

<section class="letterhead">
  <header class="letterhead__header">
    <div class="letterhead__brand">taskBeaver</div>
    <div class="letterhead__tagline">plan ahead &nbsp;|&nbsp; taskBeaver</div>
    <div class="letterhead__contact">
      <p>12, Harbor Court</p>
      <p>Lakeview, state, 480012</p>
      <p class="gap">
        <svg class="icon" width="9" height="9" viewBox="0 0 10 10"><path d="M2 1 L4 1 L4.6 3.2 L3.5 4 Q4.4 6 6 6.6 L6.8 5.5 L9 6 L9 8 Q5 9.5 2.5 6.5 Q0.5 4 2 1Z" fill="currentColor"/></svg>555-014-2273
      </p>
      <p>
        <svg class="icon" width="9" height="8" viewBox="0 0 10 8"><rect x="0.5" y="1.5" width="9" height="6" fill="currentColor"/><path d="M0.5 1.5 L5 4.5 L9.5 1.5" stroke="#81788c" stroke-width="0.8" fill="none"/></svg>info@taskBeaver.test
      </p>
    </div>
  </header>

  <svg class="letterhead__footer" width="735" height="30" viewBox="0 0 735 30">
    <rect x="0" y="12" width="520" height="7" fill="var(--rule)"/>
    <rect x="0" y="19" width="735" height="11" fill="var(--brand)"/>
    <path d="M500 19 C522 19 512 1 540 1 L735 1 L735 30 L500 30 Z" fill="var(--brand)"/>
  </svg>
  <div class="footer-url">www.taskBeaver.test</div>
</section>

<section class="card">
  <header class="card__header">
    <div class="card__brand">taskBeaver</div>
    <div class="card__tagline">plan ahead &nbsp;|&nbsp; taskBeaver</div>
    <div class="card__name">YOUR NAME</div>
  </header>
  <div class="card__contact">
    <p>
      <svg class="icon" width="11" height="11" viewBox="0 0 10 10"><path d="M2 1 L4 1 L4.6 3.2 L3.5 4 Q4.4 6 6 6.6 L6.8 5.5 L9 6 L9 8 Q5 9.5 2.5 6.5 Q0.5 4 2 1Z" fill="none" stroke="currentColor" stroke-width="0.8"/></svg>555-014-2273
    </p>
    <p>
      <svg class="icon" width="11" height="9" viewBox="0 0 10 8"><rect x="0.5" y="1.5" width="9" height="6" fill="currentColor"/><path d="M0.5 1.5 L5 4.5 L9.5 1.5" stroke="#fff" stroke-width="0.8" fill="none"/></svg>info@taskBeaver.test
    </p>
    <p class="address">12, Harbor Court, Lakeview, state, 480012</p>
  </div>
  <svg class="card__footer" width="525" height="24" viewBox="0 0 525 24">
    <rect x="0" y="10" width="310" height="4" fill="var(--rule)"/>
    <rect x="0" y="14" width="525" height="10" fill="var(--brand)"/>
    <path d="M290 14 C310 14 300 1 322 1 L525 1 L525 24 L290 24 Z" fill="var(--brand)"/>
  </svg>
  <div class="footer-url">www.taskbeaver.test</div>
</section>

</body>
</html>
```